Website for research group at university relating to human wildlife conflict

Australian university based research group. Researching the relationship between humans and wildlife, and seeking to explore ways for the two to coexist. The research group is called "Fernvale Habitat Bridging lab" (FeBri=coexistence, which should be spelled out somewhere)

I have a logo for the research group (from artmarketly). it is attached. I like it when the logo can be used throughout the website (e.g for titles, and in backgrounds).

Just a simple and clean/modern feel. i like the following websites as examples, but also like to be a little different!
https://www.brushvale.org/
http://www.qmtpna.org/

At least one large image on each page, like a banner (just put in one and i can replace them). Images of Australian wildlife preferred (especially canids), and images with humans and animals helps too.

I would like the following pages
Home page (including Vision statement; and link to twitter account).
THEN, the following pages- which can all be the same/similar design with minor differences according to content of that page.
People (inc photo and profile)
Publications (list of publications by topic)
Projects (details of projects- with title, photo, detail)
News items (by topic, with title, image, link)
Contact
Collaborators (list of groups and people we associated with group- name and photo)

Target Market(s)

government. researchers. university.

Industry/Entity Type

University

Coding

Coded - Design and coding required

Number of Pages Required

5+ page

Font styles to use
Sans Serif

Colors

Designer to choose colors to be used in the design.

Requirements
Must have
• I require all the coded files so that i have flexibility of where i can host it.
• must have my logo.
• must have a visually appealing, modern and easy to navigate landing page.
• must have a large photo (e.g banner) at the top of every page.
• must have twitter feed on home page.
Nice to have
• I require all the coded files so that i have the flexibility of where i can host it.

```html
<!DOCTYPE html>
<html lang="en">
<head>
<meta charset="utf-8">
<title>Fernvale Habitat Bridging lab</title>
<link href="https://fonts.googleapis.com/css2?family=Open+Sans:wght@400;600;700&family=Raleway:wght@600;700&family=Lora:wght@400;700&display=swap" rel="stylesheet">
<style>
:root{
  --orange:#e8743b;
  --green:#5b7f2f;
  --green-dark:#44651f;
  --green-title:#4f7a2b;
  --ink:#2b2b2b;
  --text:#555;
  --muted:#8a8a8a;
  --news-bg:#eeeef4;
  --footer:#1b1f25;
  --footer-text:#c9c9c9;
  --white:#fff;
}
*{box-sizing:border-box;margin:0;padding:0}
html,body{width:1200px;height:3429px;overflow:hidden}
body{font-family:"Open Sans",Arial,sans-serif;color:var(--text);background:var(--white);position:relative}
.abs{position:absolute}
section,header,footer{position:relative;width:1200px;overflow:hidden}
.btn{display:inline-flex;align-items:center;justify-content:center;background:var(--green);color:var(--white);font-size:12px;font-weight:600;letter-spacing:.5px;text-transform:uppercase;border-radius:4px;border-bottom:3px solid var(--orange);text-decoration:none}

/* hero */
.hero{height:652px}
.hero-photo{position:absolute;inset:0;background:
  linear-gradient(180deg,rgba(20,30,18,.55) 0%,rgba(20,30,18,.25) 45%,rgba(30,40,20,.2) 100%),
  radial-gradient(ellipse at 50% 30%,#6d7f5a 0%,#3e5233 45%,#27351f 100%)}
.hero-ground{position:absolute;left:0;right:0;bottom:0;height:200px;background:linear-gradient(180deg,rgba(90,110,50,0) 0%,#6b7d37 60%,#5e6f2e 100%)}
.brand{position:absolute;left:140px;top:22px;display:flex;align-items:center;gap:12px}
.brand-dot{width:34px;height:34px;border-radius:50%;background:var(--orange);flex:none}
.brand-name{font-weight:700;color:var(--orange);font-size:17px;line-height:1.2;width:150px}
.topbar{position:absolute;top:9px;left:718px;font-size:11px;color:#b9c0a6;display:flex;gap:30px;align-items:center}
.topbar .follow{color:var(--white);display:flex;gap:8px;align-items:center}
.sq{width:11px;height:11px;background:var(--white);border-radius:2px;display:inline-block}
.nav{position:absolute;top:50px;left:597px;font-size:13px;text-transform:uppercase}
.nav a{color:var(--white);text-decoration:none;position:absolute;white-space:nowrap}
.hero-kicker{position:absolute;top:190px;width:100%;text-align:center;font-family:"Lora",serif;color:var(--orange);font-size:42px}
.hero-title{position:absolute;top:248px;width:100%;text-align:center;font-weight:700;color:var(--white);font-size:50px;letter-spacing:1px}
.hero-lede{position:absolute;top:308px;left:310px;width:580px;text-align:center;color:var(--white);font-size:14px;line-height:23px}
.hero .btn{position:absolute;left:569px;top:372px;width:133px;height:36px}

/* about */
.about{height:514px}
.about h2{position:absolute;left:128px;top:108px;font-family:"Lora",serif;font-weight:700;font-size:27px;color:var(--ink)}
.about p{position:absolute;left:128px;top:150px;width:400px;font-size:13px;line-height:21px;color:#444}
.ticks{position:absolute;left:128px;top:285px;list-style:none;font-size:13px;color:#555}
.ticks li{display:flex;align-items:center;gap:12px;height:29px}
.about .btn{position:absolute;left:128px;top:418px;width:135px;height:41px}
.video{position:absolute;left:620px;top:82px;width:420px;height:350px;border-radius:24px;background:linear-gradient(135deg,#4e9a3e 0%,#2f7a2c 55%,#1f5f22 100%);display:flex;align-items:center;justify-content:center}
.play{width:56px;height:56px;border-radius:50%;background:var(--orange);display:flex;align-items:center;justify-content:center}

/* mission band */
.mission{height:233px}
.mission-photo{position:absolute;inset:0;background:linear-gradient(90deg,#3a2d22 0%,#5a4432 35%,#6b5440 55%,#4b3a2c 100%)}
.mission h3{position:absolute;left:137px;top:88px;color:var(--orange);font-weight:600;font-size:30px}
.mission p{position:absolute;left:137px;top:130px;color:var(--white);font-size:16px}
.mission .btn{position:absolute;left:919px;top:100px;width:135px;height:41px}

/* section titles */
.sec-head{position:absolute;left:0;width:100%;text-align:center}
.sec-head .mark{width:18px;height:18px;border-radius:50%;background:var(--orange);margin:0 auto 14px}
.sec-head h2{display:inline-flex;align-items:center;gap:18px;color:var(--orange);font-size:30px;font-weight:700;text-transform:uppercase}
.sec-head h2::before,.sec-head h2::after{content:"";width:38px;height:8px;border-top:2px solid var(--orange);border-bottom:2px solid var(--orange)}
.sec-head p{font-size:13px;color:#666;margin-top:10px}

/* projects */
.projects{height:807px;background:var(--white)}
.card{position:absolute;top:242px;width:304px;height:446px;background:var(--white);box-shadow:0 4px 14px rgba(0,0,0,.13)}
.card .photo{height:176px}
.card .badge{position:absolute;left:127px;top:169px;width:50px;height:50px;border-radius:50%;background:var(--white);box-shadow:0 0 0 3px #eee;display:flex;align-items:center;justify-content:center}
.card .badge span{width:24px;height:24px;border-radius:50%;background:var(--orange)}
.card h3{position:absolute;top:260px;width:100%;text-align:center;font-family:"Raleway",sans-serif;font-weight:600;font-size:20px;color:var(--green-title)}
.card p{position:absolute;top:302px;left:30px;right:30px;text-align:center;font-size:12px;line-height:22px;color:var(--muted)}
.card .meta{position:absolute;top:398px;left:20px;right:20px;display:flex;justify-content:space-between;font-size:11px;color:#5a7a8a;text-transform:uppercase}
.meta span{display:flex;align-items:center;gap:7px}

/* news */
.news{height:857px;background:var(--news-bg)}
.feature{position:absolute;left:135px;top:224px;width:457px;height:535px;background:var(--white);box-shadow:0 3px 12px rgba(0,0,0,.08)}
.feature .photo{height:347px}
.feature .badge{position:absolute;left:203px;top:324px;width:50px;height:50px;border-radius:50%;background:var(--white);display:flex;align-items:center;justify-content:center}
.feature .badge span{width:24px;height:24px;border-radius:50%;background:var(--orange)}
.feature h3{position:absolute;left:25px;top:383px;font-family:"Raleway",sans-serif;font-size:19px;font-weight:700;color:var(--orange)}
.feature p{position:absolute;left:25px;top:414px;width:410px;font-size:13px;line-height:23px;color:#777}
.read{font-size:13px;font-weight:600;color:#333}
.feature .read{position:absolute;left:25px;top:488px}
.brief{position:absolute;left:619px;width:462px;height:262px}
.brief .panel{position:absolute;left:150px;right:0;top:22px;height:220px;background:var(--white);box-shadow:0 3px 12px rgba(0,0,0,.08)}
.brief .photo{position:absolute;left:0;top:0;width:211px;height:100%}
.brief h3{position:absolute;left:227px;top:48px;width:220px;font-family:"Raleway",sans-serif;font-size:18px;font-weight:700;color:#222;line-height:24px}
.brief p{position:absolute;left:227px;top:104px;width:215px;font-size:12.5px;line-height:21px;color:#888}
.brief .read{position:absolute;left:227px;top:184px}

/* footer */
.site-footer{height:366px;background:var(--footer);color:var(--footer-text)}
.foot-brand{position:absolute;left:130px;top:52px;display:flex;align-items:center;gap:10px}
.foot-brand .brand-name{width:140px;font-size:15px}
.foot-lab{position:absolute;left:130px;top:202px;color:var(--orange);font-size:16px;font-weight:600}
.foot-addr{position:absolute;left:130px;top:226px;width:230px;font-size:11px;line-height:17px;color:#a5b34a}
.foot-col h4{font-size:17px;font-weight:600;color:var(--orange)}
.foot-col h4 b{color:var(--footer-text);font-weight:600}
.links{list-style:none;margin-top:14px;font-size:12px}
.links li{height:27px;display:flex;align-items:center;gap:10px}
.links li::before{content:"";width:9px;height:9px;border-radius:50%;border:2px solid var(--orange)}
.newsletter p{font-size:13px;margin-top:12px}
.newsletter .field{margin-top:16px;width:215px;height:39px;background:var(--white);border-radius:2px;color:#999;font-size:12px;display:flex;align-items:center;padding-left:12px}
.newsletter .btn{margin-top:11px;width:215px;height:39px}
.contact-list{list-style:none;margin-top:8px;font-size:12px}
.contact-list li{display:flex;gap:14px;padding:8px 0;border-bottom:1px solid #2d333b;line-height:18px}
.contact-list svg{flex:none;margin-top:3px}
.socials{display:flex;gap:14px;margin-top:20px}
.socials span{width:22px;height:22px;background:var(--white);border-radius:3px}
</style>
</head>
<body>

<header class="hero">
  <div class="hero-photo" role="img" aria-label="Photograph of a family of elephants walking across green grassland at the edge of a forest"></div>
  <div class="hero-ground" aria-hidden="true"></div>
  <div class="brand"><span class="brand-dot"></span><span class="brand-name">Fernvale Habitat Bridging lab</span></div>
  <div class="topbar"><span>Saving Today for Better Tomorrow</span><span class="follow">Follow us on: <i class="sq"></i><i class="sq"></i><i class="sq"></i></span></div>
  <nav class="nav">
    <a href="#" style="left:0">Home</a>
    <a href="#" style="left:68px">Team</a>
    <a href="#" style="left:150px">Publications</a>
    <a href="#" style="left:272px">Projects</a>
    <a href="#" style="left:336px">News</a>
    <a href="#" style="left:395px">Contact</a>
  </nav>
  <div class="hero-kicker">Journey to</div>
  <h1 class="hero-title">FERNVALE HABITAT BRIDGING LAB</h1>
  <p class="hero-lede">There are many variations of passages of Lorem Ipsum available but the majority have that suffered alteration in some form by injected humour.</p>
  <a class="btn" href="#">Learn More</a>
</header>

<section class="about">
  <h2>What is human-wildlife conflict?</h2>
  <p>Human-wildlife conflict is one of the most complex and urgent challenges for wildlife conservation around the world. It typically involves situations in which a threatened species poses a direct threat to people and their livelihoods, resulting in retaliation against the species they blame for this.</p>
  <ul class="ticks">
    <li><svg width="12" height="10" viewBox="0 0 12 10"><path d="M1 5l3.5 3.5L11 1" fill="none" stroke="#5b7f2f" stroke-width="2"/></svg>Lorem Ipsum available but the is majority have suffered.</li>
    <li><svg width="12" height="10" viewBox="0 0 12 10"><path d="M1 5l3.5 3.5L11 1" fill="none" stroke="#5b7f2f" stroke-width="2"/></svg>The available but the is majority have suffered.</li>
    <li><svg width="12" height="10" viewBox="0 0 12 10"><path d="M1 5l3.5 3.5L11 1" fill="none" stroke="#5b7f2f" stroke-width="2"/></svg>Dummy text available but the is majority have suffered.</li>
    <li><svg width="12" height="10" viewBox="0 0 12 10"><path d="M1 5l3.5 3.5L11 1" fill="none" stroke="#5b7f2f" stroke-width="2"/></svg>If you are going to use a passage of Lorem Ipsum.</li>
  </ul>
  <a class="btn" href="#">Learn More</a>
  <div class="video" role="img" aria-label="Video still of a monkey behind a wire fence in green tones">
    <span class="play"><svg width="20" height="22" viewBox="0 0 20 22"><path d="M2 1v20l17-10z" fill="#fff"/></svg></span>
  </div>
</section>

<section class="mission">
  <div class="mission-photo" role="img" aria-label="Dimmed photograph of a kangaroo in dry bushland"></div>
  <h3>Join the mission to help world</h3>
  <p>Lorem Ipsum available but the majority have that suffered alteration.</p>
  <a class="btn" href="#">Learn More</a>
</section>

<section class="projects">
  <div class="sec-head" style="top:72px">
    <div class="mark"></div>
    <h2>FeBri Projects</h2>
    <p>Lorem Ipsum is simply dummy text of the printing and typesetting industry.</p>
  </div>
  <article class="card" style="left:110px">
    <div class="photo" role="img" aria-label="Photograph of a snow leopard on a snowy forest track" style="background:linear-gradient(180deg,#5f7a6b 0%,#a9b8b3 55%,#eef1f0 100%)"></div>
    <div class="badge"><span></span></div>
    <h3>Action for Conservation</h3>
    <p>Lorem Ipsum is simply dummying of the printing and type setting industry...</p>
    <div class="meta"><span><svg width="14" height="14" viewBox="0 0 14 14"><rect x="1" y="2.5" width="12" height="10.5" rx="1" fill="none" stroke="#5a7a8a"/><path d="M1 6h12M4 1v3M10 1v3" stroke="#5a7a8a"/></svg>23 May 2017</span><span><svg width="10" height="12" viewBox="0 0 10 12"><path d="M1 1l8 5-8 5z" fill="none" stroke="#5a7a8a"/></svg>Read More</span></div>
  </article>
  <article class="card" style="left:462px">
    <div class="photo" role="img" aria-label="Photograph of a child in a sun hat feeding a camel at a fence" style="background:linear-gradient(180deg,#b4745a 0%,#c89c7e 50%,#f2ebe4 100%)"></div>
    <div class="badge"><span></span></div>
    <h3>Andean Bear Project</h3>
    <p>Lorem Ipsum is simply dummying of the printing and type setting industry...</p>
    <div class="meta"><span><svg width="14" height="14" viewBox="0 0 14 14"><rect x="1" y="2.5" width="12" height="10.5" rx="1" fill="none" stroke="#5a7a8a"/><path d="M1 6h12M4 1v3M10 1v3" stroke="#5a7a8a"/></svg>23 May 2017</span><span><svg width="10" height="12" viewBox="0 0 10 12"><path d="M1 1l8 5-8 5z" fill="none" stroke="#5a7a8a"/></svg>Read More</span></div>
  </article>
  <article class="card" style="left:798px">
    <div class="photo" role="img" aria-label="Photograph of deer grazing on a field in front of trees" style="background:linear-gradient(180deg,#dfe6ea 0%,#5f7a4a 35%,#8a8a5e 65%,#f4f2ee 100%)"></div>
    <div class="badge"><span></span></div>
    <h3>Badger Projectv</h3>
    <p>Lorem Ipsum is simply dummying of the printing and type setting industry...</p>
    <div class="meta"><span><svg width="14" height="14" viewBox="0 0 14 14"><rect x="1" y="2.5" width="12" height="10.5" rx="1" fill="none" stroke="#5a7a8a"/><path d="M1 6h12M4 1v3M10 1v3" stroke="#5a7a8a"/></svg>23 May 2017</span><span><svg width="10" height="12" viewBox="0 0 10 12"><path d="M1 1l8 5-8 5z" fill="none" stroke="#5a7a8a"/></svg>Read More</span></div>
  </article>
</section>

<section class="news">
  <div class="sec-head" style="top:60px">
    <div class="mark"></div>
    <h2>Latest News</h2>
    <p>Lorem Ipsum is simply dummy text of the printing and typesetting industry.</p>
  </div>
  <article class="feature">
    <div class="photo" role="img" aria-label="Photograph of elephants on bright green grass in a sunlit forest" style="background:linear-gradient(180deg,#c9d59a 0%,#7d8f4a 40%,#55632e 70%,#8fb33a 100%)"></div>
    <div class="badge"><span></span></div>
    <h3>Rowan: an orangutan known &amp; loved</h3>
    <p>There are many variations of passages of Lorem Ipsum available to but the majority have suffered alteration in some form by in- jected humour or randomised words which.</p>
    <span class="read">Read More</span>
  </article>
  <article class="brief" style="top:208px">
    <div class="panel"></div>
    <div class="photo" role="img" aria-label="Photograph of a red kangaroo standing and facing forward" style="background:linear-gradient(180deg,#c06a3a 0%,#a9542d 50%,#c98a4e 100%)"></div>
    <h3>Contrast for color of poison dart panda</h3>
    <p>There are many variations of dummy passages of Lorem Ipsum available to but the majority.</p>
    <span class="read">Read More</span>
  </article>
  <article class="brief" style="top:516px">
    <div class="panel"></div>
    <div class="photo" role="img" aria-label="Photograph of a kangaroo leaping across red desert under a blue sky" style="background:linear-gradient(180deg,#7d9bc9 0%,#a9bfdc 55%,#c68a4a 80%,#b0652e 100%)"></div>
    <h3>Contrast for color of poison dart panda</h3>
    <p>There are many variations of dummy passages of Lorem Ipsum available to but the majority.</p>
    <span class="read">Read More</span>
  </article>
</section>

<footer class="site-footer">
  <div class="foot-brand"><span class="brand-dot"></span><span class="brand-name">Fernvale Habitat Bridging lab</span></div>
  <div class="foot-lab">FeBri Lab</div>
  <div class="foot-addr">Department of Zoology,<br>University of Tarrowind,<br>Marlow Field Centre, Kestrel House,<br>Birchgate Road, Ellory, QLD 4210</div>

  <div class="foot-col abs" style="left:402px;top:84px">
    <h4>Quick <b>Links</b></h4>
    <ul class="links"><li>Home</li><li>Team</li><li>Publications</li><li>Projects</li><li>News</li><li>Contact</li></ul>
  </div>

  <div class="foot-col newsletter abs" style="left:592px;top:84px">
    <h4><b>Our</b> Newsletter</h4>
    <p>Subcribe and get our news &amp; update</p>
    <div class="field">Email</div>
    <a class="btn" href="#">Subscribe</a>
  </div>

  <div class="foot-col abs" style="left:892px;top:84px;width:230px">
    <h4>STAY IN <b>TOUCH</b></h4>
    <ul class="contact-list">
      <li><svg width="10" height="13" viewBox="0 0 10 13"><path d="M5 12S1 7.5 1 5a4 4 0 018 0c0 2.5-4 7-4 7z" fill="#ccc"/><circle cx="5" cy="5" r="1.5" fill="#1b1f25"/></svg>48 Saltbush Lane Wyndell Creek Road, Wyndell, QLD, 4307</li>
      <li><svg width="12" height="12" viewBox="0 0 12 12"><path d="M2 1l2.5 0 1 3-1.5 1a7 7 0 003 3l1-1.5 3 1V11A10 10 0 011 2z" fill="#ccc"/></svg>+ 61 7 5550 1842</li>
      <li><svg width="13" height="10" viewBox="0 0 13 10"><rect x=".5" y=".5" width="12" height="9" fill="none" stroke="#ccc"/><path d="M.5 .5l6 5 6-5" fill="none" stroke="#ccc"/></svg>info@febrilab.org</li>
    </ul>
    <h4 style="margin-top:14px">GET SOCIAL <b>WITH US</b></h4>
    <div class="socials"><span></span><span></span><span></span></div>
  </div>
</footer>

</body>
</html>
```